fun theme dental practice website!

This client LOVES their superhero theme! They are an established pediatric dental practice with multiple locations. They have recently expanded to see adults and do orthodontics. They would like to have a new website design for the adult part of their practice. It should be similar in theme (superhero) but more adult (no sugarbugs!) . Navigation: about, meet the team, treatments, orthodontics, contact
add appointment request feature

Target Market(s)

adults

Industry/Entity Type

Dental

Number of Pages Required

2 page

Requirements
Must have
• home page design and interior page design
• fun and in theme but not too babyish (should it still look like a comic book?)
• appointment request feature
• visual pow
• colors consistent with logo (see attached)
• use the tooth social media icons

```html
<!DOCTYPE html>
<html lang="en">
<head>
<meta charset="utf-8">
<title>Schedule an appointment – Valor Dental &amp; Orthodontics</title>
<link href="https://fonts.googleapis.com/css2?family=Montserrat:ital,wght@0,400;0,500;0,600;0,700;1,500&display=swap" rel="stylesheet">
<style>
  :root {
    --green: #8cc63f;
    --green-dark: #4f9a1c;
    --red: #e31e24;
    --ink: #333333;
    --muted: #6b6b6b;
    --line: #3a3a3a;
    --page: #f3f3f3;
    --white: #ffffff;
  }
  * { box-sizing: border-box; margin: 0; padding: 0; }
  html, body { width: 1200px; height: 750px; overflow: hidden; }
  body {
    position: relative;
    background: var(--page);
    font-family: "Montserrat", Arial, sans-serif;
    color: var(--ink);
  }
  .site-header {
    position: absolute; left: 0; top: 0; width: 1200px; height: 74px;
    background: var(--green);
    box-shadow: 0 2px 0 #9aa79a;
  }
  .brand {
    position: absolute; left: 40px; top: 18px;
    display: flex; align-items: center; gap: 8px;
    font-weight: 700; font-size: 14px; line-height: 18px; color: var(--white);
    white-space: nowrap;
  }
  .brand-mark { width: 22px; height: 22px; background: var(--red); border-radius: 50%; flex: none; }
  .main-nav a {
    position: absolute; top: 28px;
    font-size: 12.5px; font-weight: 500; letter-spacing: 0.6px;
    color: var(--white); text-decoration: none; text-transform: uppercase;
    white-space: nowrap;
  }
  .main-nav a.is-current { color: var(--green-dark); }
  .page-title {
    position: absolute; left: 0; top: 114px; width: 1200px;
    text-align: center; font-size: 35px; font-weight: 500; color: var(--ink);
  }
  .field {
    position: absolute;
    border-bottom: 2px solid var(--line);
    font-size: 19.5px; color: var(--muted);
  }
  .field-label-only {
    position: absolute; font-size: 19.5px; color: var(--muted);
  }
  .group-label {
    position: absolute; font-size: 17px; font-weight: 500; color: var(--ink);
  }
  .date-part {
    position: absolute; top: 438px; height: 26px;
    border-bottom: 2px solid var(--line);
    font-size: 17px; color: var(--muted);
  }
  .type-switch {
    position: absolute; left: 105px; top: 514px; height: 24px;
    display: flex; border-radius: 4px; overflow: hidden;
  }
  .type-option {
    height: 24px; line-height: 24px; font-size: 14px; font-weight: 500;
    color: var(--white); background: #3a3a3a; text-align: center;
  }
  .type-option.is-active { background: var(--green); }
  .submit-button {
    position: absolute; left: 105px; top: 575px; width: 98px; height: 46px;
    border: 0; border-radius: 4px; background: var(--red);
    color: var(--white); font-family: inherit; font-size: 18px; font-weight: 700;
  }
  .form-status {
    position: absolute; left: 227px; top: 585px;
    font-size: 18px; font-weight: 500; line-height: 26px; white-space: nowrap;
  }
  .status-success { color: var(--green); }
  .status-error { color: var(--red); }
  .status-error em { font-style: italic; }
  .site-footer {
    position: absolute; left: 0; top: 701px; width: 1200px;
    text-align: center; font-size: 19px; font-weight: 500; color: var(--muted);
  }
</style>
</head>
<body>
  <header class="site-header">
    <div class="brand"><span class="brand-mark"></span><span>Valor<br>Dental &amp; Orthodontics</span></div>
    <nav class="main-nav">
      <a href="#" style="left:319px">About</a>
      <a href="#" class="is-current" style="left:411px">Meet the team</a>
      <a href="#" style="left:565px">Schedule an appointment</a>
      <a href="#" style="left:810px">Treatments</a>
      <a href="#" style="left:942px">Orthodontics</a>
      <a href="#" style="left:1093px">Contact</a>
    </nav>
  </header>

  <main>
    <h1 class="page-title">Schedule an appointment</h1>

    <div class="field" style="left:103px; top:215px; width:400px; height:29px;">full name</div>
    <div class="field" style="left:103px; top:268px; width:401px; height:29px;">phone</div>
    <div class="field" style="left:103px; top:321px; width:401px; height:29px;">email address</div>

    <div class="field" style="left:764px; top:217px; width:401px; height:29px;">reason</div>
    <div class="field-label-only" style="left:763px; top:268px;">note for us</div>
    <div class="field" style="left:764px; top:300px; width:401px; height:50px;"></div>

    <div class="group-label" style="left:103px; top:396px;">Date of birth</div>
    <div class="date-part" style="left:104px; width:46px;">DD</div>
    <div class="date-part" style="left:157px; width:46px;">MM</div>
    <div class="date-part" style="left:217px; width:45px;">YY</div>

    <div class="group-label" style="left:763px; top:396px;">Date of visit</div>
    <div class="date-part" style="left:764px; width:45px;">DD</div>
    <div class="date-part" style="left:816px; width:46px;">MM</div>
    <div class="date-part" style="left:877px; width:45px;">YY</div>

    <div class="type-switch">
      <div class="type-option" style="width:87px">Type #1</div>
      <div class="type-option" style="width:87px">Type #2</div>
      <div class="type-option is-active" style="width:88px">Type #3</div>
    </div>

    <button class="submit-button" type="button">submit</button>

    <div class="form-status">
      <p class="status-success">The form has been submitted successfully!</p>
      <p class="status-error"><em>We're sorry</em>: The email address you have provided is invalid. The date of visit is no longer available.<br>Please choose a different date.</p>
    </div>
  </main>

  <footer class="site-footer">Valor Dental &amp; Orthodontics © 2016</footer>
</body>
</html>
```